Best local air conditioning and heating contractor

We need a website design for a new company in Tampa Bay called the Summit Breeze Cooling Company. We provide superior services for residential and commercial properties as well as maintenance and installing HVAC systems. We also want to sell equipment, parts and filter on the website as well. We want it easy to use for customers. Rich with content and keywords for our area.

Target Market(s)

homeowners in Tampa Bay

Industry/Entity Type

HVAC air conditioning and heating

Coding

Coded - Design and coding required

Number of Pages Required

5+ page

Font styles to use
Sans Serif

Requirements
Nice to have
• would like the colors to be same as logo

```html
<!DOCTYPE html>
<html lang="en">
<head>
<meta charset="utf-8">
<title>Contact Us – Summit Breeze Cooling Company</title>
<link href="https://fonts.googleapis.com/css2?family=Michroma&family=Outfit:wght@400;500;600;700;800&display=swap" rel="stylesheet">
<style>
:root{
  --navy:#27305e;
  --navy-deep:#1f2750;
  --red:#d6262b;
  --ink:#111111;
  --text:#2a2a2a;
  --line:#d9d9d9;
  --white:#ffffff;
  --star:#f6c42a;
}
*{margin:0;padding:0;box-sizing:border-box}
html,body{width:796px;height:1200px;overflow:hidden}
body{position:relative;font-family:"Outfit",sans-serif;color:var(--text);background:var(--white)}
.abs{position:absolute}

/* top bar */
.topbar{left:0;top:0;width:796px;height:19px;background:var(--navy);color:var(--white);font-size:8px;font-weight:500}
.topbar .stars{left:67px;top:4px;color:var(--star);font-size:8px;letter-spacing:-0.5px}
.topbar .rating{left:113px;top:5px}
.topbar .sep{top:3px;width:1px;height:13px;background:rgba(255,255,255,.35)}
.topbar .hours{left:249px;top:5px;display:flex;align-items:center;gap:3px}
.topbar .area{right:150px;top:5px;display:flex;align-items:center;gap:3px}
.topbar .social{top:5px;width:8px;height:8px;border:1.2px solid var(--white);border-radius:50%}

/* header */
.header{left:0;top:19px;width:796px;height:51px;background:var(--white)}
.brand{left:67px;top:9px;display:flex;align-items:center;gap:5px}
.brand .dot{width:14px;height:14px;border-radius:50%;background:var(--navy)}
.brand .name{font-weight:800;font-size:10px;line-height:11px;color:var(--navy);text-transform:uppercase;width:100px}
.nav{top:21px;font-size:9.5px;font-weight:600;color:var(--ink);text-transform:uppercase}
.callbox{left:586px;top:0;width:210px;height:51px;background:var(--red);clip-path:polygon(14px 0,100% 0,100% 100%,0 100%)}
.callbox .ring{left:8px;top:10px;width:30px;height:30px;border-radius:50%;background:var(--navy);border:2px solid var(--white)}
.callbox .label{left:34px;top:7px;color:var(--white);font-size:11px}
.callbox .number{left:34px;top:21px;color:var(--white);font-size:20px;font-weight:800;letter-spacing:.3px}

/* hero */
.hero{left:0;top:70px;width:796px;height:207px;background:linear-gradient(100deg,#7a6a5c 0%,#3a3d44 25%,#2c2f36 55%,#3a3b40 75%,#8c6a6e 100%)}
.hero::after{content:"";position:absolute;inset:0;background:rgba(20,22,35,.35)}
.hero-title{left:0;top:176px;width:796px;text-align:center;font-family:"Michroma",sans-serif;font-size:23px;color:var(--white);letter-spacing:1px;z-index:2}

/* get in touch */
.section-title{left:0;top:318px;width:796px;text-align:center;font-family:"Michroma",sans-serif;font-size:23px;color:var(--ink)}
.section-title .accent{color:var(--red)}
.underline{left:369px;top:347px;width:58px;height:2px;background:var(--red)}

.intro{left:67px;top:380px;width:303px;font-size:9.6px;line-height:17px;text-align:justify}

.card{left:66px;width:314px;height:61px;background:var(--white);box-shadow:0 0 6px rgba(0,0,0,.09)}
.card .icon{left:17px;top:12px;width:37px;height:37px;border-radius:50%;border:1px solid var(--red);display:flex;align-items:center;justify-content:center}
.card .title{left:62px;top:16px;font-size:10.5px;font-weight:600;color:var(--ink);text-transform:uppercase}
.card .detail{left:62px;top:33px;font-size:10.5px;color:var(--ink)}

/* form */
.form-panel{left:394px;top:376px;width:336px;height:294px;background:var(--white);box-shadow:0 0 6px rgba(0,0,0,.09)}
.form-title{left:409px;top:400px;font-size:20.5px;font-weight:700;color:var(--ink)}
.field{border:1px solid var(--line);background:var(--white);font-size:9px;color:var(--ink);padding:9px 9px}
.submit{left:613px;top:617px;width:107px;height:29px;background:var(--red);color:var(--white);font-size:10.5px;font-weight:700;display:flex;align-items:center;justify-content:center;text-transform:uppercase}

/* map */
.map{left:0;top:722px;width:796px;height:238px;background:linear-gradient(135deg,#eceff1 0%,#e4e7ea 50%,#eef0f2 100%)}
.map-rule{left:0;top:960px;width:796px;height:3px;background:var(--red)}

/* footer */
.footer{left:0;top:963px;width:796px;height:237px;background:linear-gradient(180deg,var(--navy) 0%,var(--navy-deep) 100%);color:var(--white)}
.footer-brand{left:70px;top:1020px;display:flex;align-items:center;gap:6px}
.footer-brand .dot{width:22px;height:22px;border-radius:50%;background:var(--white)}
.footer-brand .name{font-weight:800;font-size:15px;line-height:16px;color:var(--white);text-transform:uppercase;width:150px}
.footer-social{top:1090px;width:25px;height:25px;border-radius:50%;background:var(--white)}
.col-title{top:1002px;font-size:12.5px;font-weight:600;color:var(--white)}
.col-item{font-size:9px;color:var(--white)}
.footer-rule{left:66px;top:1157px;width:664px;height:1px;background:rgba(255,255,255,.35)}
.copyright{left:0;top:1172px;width:796px;text-align:center;font-size:10px;color:var(--white)}
</style>
</head>
<body>

<!-- top bar -->
<div class="abs topbar">
  <span class="abs stars">★★★★★</span>
  <span class="abs rating">4.8 STAR SERVICES (20REVIEWS)</span>
  <span class="abs sep" style="left:243px"></span>
  <span class="abs hours">
    <svg width="7" height="7" viewBox="0 0 10 10"><circle cx="5" cy="5" r="4" fill="none" stroke="#d6262b" stroke-width="1.4"/><path d="M5 2.5V5h2" fill="none" stroke="#d6262b" stroke-width="1.2"/></svg>
    Mon to Fri 9:00 am to 6:00 pm
  </span>
  <span class="abs area">
    <svg width="6" height="8" viewBox="0 0 10 14"><path d="M5 0a5 5 0 0 0-5 5c0 4 5 9 5 9s5-5 5-9a5 5 0 0 0-5-5z" fill="#d6262b"/></svg>
    Serving The Tampa Bay Area
  </span>
  <span class="abs sep" style="left:651px"></span>
  <span class="abs social" style="left:657px"></span>
  <span class="abs sep" style="left:671px"></span>
  <span class="abs social" style="left:677px"></span>
  <span class="abs sep" style="left:693px"></span>
  <span class="abs social" style="left:699px"></span>
  <span class="abs sep" style="left:714px"></span>
  <span class="abs social" style="left:721px"></span>
</div>

<!-- header -->
<header class="abs header">
  <div class="abs brand"><span class="dot"></span><span class="name">Summit Breeze Cooling Company</span></div>
  <span class="abs nav" style="left:249px">About Us</span>
  <span class="abs nav" style="left:317px">Services</span>
  <span class="abs nav" style="left:382px">HVAC</span>
  <span class="abs nav" style="left:430px">Resources</span>
  <span class="abs nav" style="left:506px">Contact</span>
  <div class="abs callbox">
    <div class="abs ring" style="display:flex;align-items:center;justify-content:center">
      <svg width="13" height="13" viewBox="0 0 24 24"><path d="M6.6 10.8a15 15 0 0 0 6.6 6.6l2.2-2.2a1 1 0 0 1 1-.25 11.4 11.4 0 0 0 3.6.57 1 1 0 0 1 1 1V20a1 1 0 0 1-1 1A17 17 0 0 1 3 4a1 1 0 0 1 1-1h3.5a1 1 0 0 1 1 1c0 1.25.2 2.45.57 3.57a1 1 0 0 1-.25 1z" fill="#fff"/></svg>
    </div>
    <span class="abs label">Call Today for Service</span>
    <span class="abs number">727 - 555 - 0148</span>
  </div>
</header>

<!-- hero -->
<div class="abs hero" role="img" aria-label="Photo of outdoor air conditioning condenser units beside a house wall"></div>
<h1 class="abs hero-title">CONTACT US</h1>

<!-- get in touch -->
<h2 class="abs section-title">GET IN <span class="accent">TOUCH</span></h2>
<div class="abs underline"></div>

<p class="abs intro">Proudly Serving: Oldsmar, Palm Harbor, Tarpon Springs, Clearwater, Dunedin, Safety Harbor, Town n Country, Westchase, Waterchase, The Eagles, Countryway, The Eagles, Eastlake, West Tampa a/c repair air conditioning repair service home ac repair</p>

<div class="abs card" style="top:461px">
  <div class="abs icon"><svg width="13" height="17" viewBox="0 0 10 14"><path d="M5 0a5 5 0 0 0-5 5c0 4 5 9 5 9s5-5 5-9a5 5 0 0 0-5-5zm0 7a2 2 0 1 1 0-4 2 2 0 0 1 0 4z" fill="#d6262b"/></svg></div>
  <span class="abs title">The Summit Breeze Cooling Company</span>
  <span class="abs detail">Tampa, Florida, United States</span>
</div>
<div class="abs card" style="top:536px">
  <div class="abs icon"><svg width="17" height="17" viewBox="0 0 24 24"><path d="M6.6 10.8a15 15 0 0 0 6.6 6.6l2.2-2.2a1 1 0 0 1 1-.25 11.4 11.4 0 0 0 3.6.57 1 1 0 0 1 1 1V20a1 1 0 0 1-1 1A17 17 0 0 1 3 4a1 1 0 0 1 1-1h3.5a1 1 0 0 1 1 1c0 1.25.2 2.45.57 3.57a1 1 0 0 1-.25 1z" fill="#d6262b"/></svg></div>
  <span class="abs title">Call Us</span>
  <span class="abs detail">727-555-0148</span>
</div>
<div class="abs card" style="top:610px">
  <div class="abs icon"><svg width="19" height="13" viewBox="0 0 20 14"><rect x="0" y="0" width="20" height="14" rx="1" fill="#d6262b"/><path d="M1 1l9 7 9-7" fill="none" stroke="#fff" stroke-width="1.4"/></svg></div>
  <span class="abs title">Email</span>
  <span class="abs detail">hello@summitbreezecooling.com</span>
</div>

<!-- form -->
<div class="abs form-panel"></div>
<h3 class="abs form-title">Send a Message</h3>
<div class="abs field" style="left:406px;top:442px;width:153px;height:31px">First Name</div>
<div class="abs field" style="left:567px;top:442px;width:153px;height:31px">Last Name</div>
<div class="abs field" style="left:406px;top:481px;width:153px;height:31px">Email Address</div>
<div class="abs field" style="left:567px;top:481px;width:153px;height:31px">Phone Number</div>
<div class="abs field" style="left:406px;top:523px;width:314px;height:82px">Message</div>
<div class="abs submit">Submit »</div>

<!-- map -->
<div class="abs map" role="img" aria-label="Street map showing the company's service location"></div>
<div class="abs map-rule"></div>

<!-- footer -->
<footer class="abs footer"></footer>
<div class="abs footer-brand"><span class="dot"></span><span class="name">Summit Breeze Cooling Company</span></div>
<span class="abs footer-social" style="left:87px"></span>
<span class="abs footer-social" style="left:122px"></span>
<span class="abs footer-social" style="left:157px"></span>
<span class="abs footer-social" style="left:191px"></span>

<span class="abs col-title" style="left:310px">Quick Links</span>
<span class="abs col-item" style="left:310px;top:1026px">Home</span>
<span class="abs col-item" style="left:310px;top:1046px">About Us</span>
<span class="abs col-item" style="left:310px;top:1067px">Services</span>
<span class="abs col-item" style="left:310px;top:1087px">Hvac</span>
<span class="abs col-item" style="left:310px;top:1107px">Resources</span>
<span class="abs col-item" style="left:310px;top:1128px">Contact</span>

<span class="abs col-title" style="left:434px">Our Services</span>
<span class="abs col-item" style="left:434px;top:1026px">AC Repair</span>
<span class="abs col-item" style="left:434px;top:1046px">AC Installation</span>
<span class="abs col-item" style="left:434px;top:1067px">HVAC Maintenance</span>
<span class="abs col-item" style="left:434px;top:1087px">Duct Services</span>

<span class="abs col-title" style="left:574px">Contact Info</span>
<span class="abs col-item" style="left:574px;top:1026px">Tampa, Florida, United States</span>
<span class="abs col-item" style="left:574px;top:1047px">727-555-0148</span>
<span class="abs col-item" style="left:574px;top:1068px">hello@summitbreezecooling.com</span>

<div class="abs footer-rule"></div>
<p class="abs copyright">©Copyright 2024 The Summit Breeze Cooling Company. All Rights Reserved.</p>

</body>
</html>
```